Business Card Design for Animal Clinic

We are seeking a two sided business card design. The primary side should include our logo (provided in AI and EPS files) address, phone, website, and if possible "Follow Us" with icons for Facebook, Google+, and Twitter.

The back of the card needs to included space for appointment reminders.

Company Name:
Calderbrook Animal Clinic

Doctor Name:
To be provided to winner

Adress:
To be provided to winner

Phone:
to be provided to winner

Website:
www.calderbrookanimalclinic.com

```html
<!DOCTYPE html>
<html lang="en">
<head>
<meta charset="utf-8">
<title>Calderbrook Animal Clinic – Business Card</title>
<link href="https://fonts.googleapis.com/css2?family=Bitter:wght@300&display=swap" rel="stylesheet">
<style>
  :root {
    --card-red: #9e1c20;
    --ink-white: #ffffff;
    --cream: #f2e2da;
  }
  html, body {
    margin: 0;
    padding: 0;
    width: 1200px;
    height: 686px;
    overflow: hidden;
    background: var(--card-red);
  }
  .card {
    position: relative;
    width: 1200px;
    height: 686px;
    background: var(--card-red);
    color: var(--ink-white);
    font-family: "Bitter", Georgia, serif;
    font-weight: 300;
  }
  .brand {
    position: absolute;
    left: 0;
    top: 150px;
    width: 1200px;
    text-align: center;
  }
  .brand-name {
    margin: 0;
    font-size: 86px;
    line-height: 1;
    letter-spacing: 5px;
    font-weight: 300;
  }
  .brand-sub {
    display: flex;
    justify-content: center;
    align-items: center;
    gap: 34px;
    margin-top: 28px;
    font-size: 42px;
    letter-spacing: 5px;
    line-height: 1;
  }
  .brand-dot {
    width: 110px;
    height: 110px;
    border-radius: 50%;
    background: var(--cream);
  }
  .rule {
    position: absolute;
    left: 240px;
    width: 720px;
    height: 0;
    border-top: 2px dashed var(--ink-white);
  }
  .rule--top { top: 504px; }
  .rule--bottom { top: 574px; }
  .contact {
    position: absolute;
    top: 512px;
    font-size: 22px;
    line-height: 28px;
  }
  .contact--address {
    right: 628px;
    text-align: right;
  }
  .contact--reach {
    left: 621px;
    top: 516px;
    line-height: 23px;
  }
  .divider {
    position: absolute;
    left: 586px;
    top: 516px;
  }
  .follow {
    position: absolute;
    left: 0;
    top: 596px;
    width: 1200px;
    display: flex;
    justify-content: center;
    align-items: center;
    gap: 8px;
    font-size: 22px;
  }
  .follow-label { margin-right: 8px; }
  .social-dot {
    width: 40px;
    height: 40px;
    border-radius: 50%;
    background: var(--ink-white);
  }
</style>
</head>
<body>
  <main class="card">
    <header class="brand">
      <h1 class="brand-name">CALDERBROOK</h1>
      <div class="brand-sub">
        <span>ANIMAL</span>
        <span class="brand-dot"></span>
        <span>CLINIC</span>
      </div>
    </header>

    <div class="rule rule--top"></div>

    <address class="contact contact--address" style="font-style:normal">
      418 N. Fernhill Road<br>
      Calder Springs, FL 32790
    </address>

    <svg class="divider" width="28" height="48" viewBox="0 0 28 48" aria-hidden="true">
      <line x1="24" y1="2" x2="4" y2="46" stroke="#ffffff" stroke-width="3"/>
    </svg>

    <div class="contact contact--reach">
      (407) 555-0142<br>
      www.calderbrookanimalclinic.com
    </div>

    <div class="rule rule--bottom"></div>

    <div class="follow">
      <span class="follow-label">Follow us:</span>
      <span class="social-dot" role="img" aria-label="Social network link"></span>
      <span class="social-dot" role="img" aria-label="Social network link"></span>
      <span class="social-dot" role="img" aria-label="Social network link"></span>
    </div>
  </main>
</body>
</html>
```